Web design for boutique law firm

Web design for law firm; practice areas include:
-international intellectual property counseling
-general corporate (contract negotiation, licensing, distribution agreements
-see my *very* outdated website at www.pvtlegalhouse.com: here is some of the home page content:

"PVT Law Group enjoys providing proactive, business-minded, efficient legal solutions for individuals and companies that benefit from major law firm experience at reasonable rates.

Some areas of emphasis include:

Counseling individuals and companies with respect to clearing, selecting, securing, managing, commercializing, and protecting intellectual property assets around the world. This includes traditional global brand management, marketing, advertising, and enforcement work as well as litigation.
PVT Law Group also provides general counseling services for individuals and businesses, from start-up advice to sophisticated business transactions strategy, agreement negotiating, dispute resolution, and litigation.
Before founding PVT Law Group in 2008, Curtis L. Abernathy led the Trademark, Copyright, & Brand Management Group for Falkner & Ingleby's Seattle office. Curtis was also a senior associate at Silicon Valley based Hartwell, Bexley, Oduya, & Penrose."

Target Market(s)

Clients/potential clients needing tier one, international intellectual property advice with "mega" law firm experience for much less than what we were/would be charging at the "mega firms".

Industry/Entity Type

Legal

Number of Pages Required

4 page

Font styles to use
Serif
Sans Serif

Colors

Designer to choose colors to be used in the design.

Requirements
Must have
• +Improvement over everything on current site at www.pvtlegalhouse.com.
• +Pictures/bios for me and my team (four of us right now).
• +Easy to update and add/remove content.
• +Must be superior in design (look, feel, ease of use, classy and elegant, but hip, reflects international practice).
• +i have logos and color schemes (see current website) but will consider improvements.
Nice to have
• Let me know your thoughts.
Should not have
• No cheese; no overt sales pitches or marketing (since law firm).

```html
<!DOCTYPE html>
<html lang="en">
<head>
<meta charset="utf-8">
<title>PVT Law Group PLLC</title>
<link href="https://fonts.googleapis.com/css2?family=Montserrat:wght@300;400;600;700&family=Open+Sans:wght@400;600;700&family=Playfair+Display:wght@700&display=swap" rel="stylesheet">
<style>
:root{
  --orange:#f07022;
  --charcoal:#4a4a4a;
  --ink:#333333;
  --muted:#7a7a7a;
  --teal:#1a8f8a;
  --light:#eeeeee;
  --white:#ffffff;
  --night:#3a3a3a;
}
*{margin:0;padding:0;box-sizing:border-box}
html,body{width:1200px;height:4100px;overflow:hidden}
body{position:relative;background:var(--white);font-family:"Open Sans",Arial,sans-serif;color:var(--ink)}
.abs{position:absolute}

/* header */
.brand{left:77px;top:28px;font-family:"Montserrat",sans-serif;font-weight:400;font-size:38px;color:var(--orange);letter-spacing:1px;white-space:nowrap}
.brand-rule{left:77px;top:80px;width:334px;height:2px;background:var(--orange)}
.contact-bar{left:744px;top:14px;width:3px;height:82px;background:var(--orange)}
.contact-lines{left:757px;top:14px;font-family:"Montserrat",sans-serif;font-size:16px;line-height:27px;color:var(--charcoal);letter-spacing:.5px;white-space:nowrap}

/* nav */
.nav{left:0;top:110px;width:1200px;height:48px;background:var(--orange)}
.nav a{position:absolute;top:15px;font-family:"Montserrat",sans-serif;font-size:13px;color:var(--white);text-decoration:none;text-transform:uppercase;white-space:nowrap}

/* hero */
.hero{left:0;top:158px;width:1200px;height:525px;background:linear-gradient(120deg,#5a5550 0%,#8c8680 30%,#d8d4cf 55%,#a69a8c 80%,#6b5a48 100%);clip-path:polygon(0 0,100% 0,100% 72%,0 100%)}
.hero-edge{left:0;top:158px;width:1200px;height:525px}
.hero-card{left:724px;top:300px;width:410px;height:150px;background:rgba(40,40,40,.82);padding:14px 20px}
.hero-card h1{font-family:"Montserrat",sans-serif;font-weight:400;font-size:31px;line-height:38px;color:var(--white);text-transform:uppercase}
.btn-orange{display:inline-block;background:var(--orange);color:var(--white);font-family:"Montserrat",sans-serif;font-size:14px;text-transform:uppercase;padding:8px 16px}
.hero-card .btn-orange{margin-top:12px}

/* about */
.about-title{left:101px;top:857px;font-family:"Montserrat",sans-serif;font-size:29px;color:var(--ink);white-space:nowrap}
.about-title b{font-weight:700}
.about-title span{font-weight:300}
.about-rule{left:101px;top:902px;width:63px;height:3px;background:var(--teal)}
.about-photo{left:104px;top:929px;width:147px;height:99px;background:linear-gradient(135deg,#7a5a3e,#c9a07a,#5b6d7e)}
.about-sub{left:265px;top:932px;font-family:"Montserrat",sans-serif;font-weight:700;font-size:15px;color:var(--ink)}
.about-lead{left:265px;top:956px;width:470px;font-size:15px;line-height:23px;color:var(--muted)}
.about-body{left:101px;top:1038px;width:560px;font-size:15px;line-height:24px;color:var(--muted)}
.read-more{font-family:"Montserrat",sans-serif;font-size:13px;font-weight:600;color:var(--teal);white-space:nowrap}
.about-more{left:101px;top:1136px}

/* question form */
.ask{left:779px;top:773px;width:325px;height:380px;background:var(--orange);padding:30px 22px}
.ask h2{font-family:"Montserrat",sans-serif;font-weight:700;font-size:25px;color:var(--white);text-transform:uppercase;white-space:nowrap;text-align:center}
.field{background:var(--white);height:42px;margin-top:0;padding:0 12px;font-size:13px;line-height:42px;color:#999}
.ask .field{position:absolute;left:24px;width:277px}
.ask .btn-dark{position:absolute;left:24px;top:295px;width:277px;height:47px;background:#1f1f1f;color:var(--white);font-family:"Montserrat",sans-serif;font-size:16px;line-height:47px;text-align:center;text-transform:uppercase}

/* shared section headings */
.sec-title{left:0;width:1200px;text-align:center;font-family:"Montserrat",sans-serif;font-weight:700;font-size:29px}
.divider{left:270px;width:660px;height:30px}

/* services */
.services{left:0;top:1257px;width:1200px;height:574px;background:var(--charcoal);clip-path:polygon(0 96px,100% 0,100% 92%,0 100%)}
.services .sec-title{color:var(--white);top:105px}
.svc{top:215px;width:250px;text-align:center;color:var(--white)}
.svc-icon{width:104px;height:104px;border-radius:50%;background:var(--orange);border:3px solid #f48b4c;margin:0 auto;display:flex;align-items:center;justify-content:center}
.svc h3{font-family:"Montserrat",sans-serif;font-weight:600;font-size:21px;margin-top:22px;white-space:nowrap}
.svc p{font-size:13px;line-height:20px;margin:14px auto 0;width:228px;color:#f0f0f0}
.svc .read-more{display:inline-block;color:var(--white);font-size:12px;margin-top:14px;padding:4px 8px}
.svc .read-more.boxed{border:1px solid var(--white)}

/* attorneys */
.team .sec-title{color:var(--ink)}
.attorney{top:2069px;width:232px;text-align:center}
.attorney-photo{width:232px;height:282px;clip-path:polygon(0 0,100% 0,100% 100%,0 88%)}
.attorney h3{font-family:"Open Sans",sans-serif;font-weight:400;font-size:20px;color:var(--ink);margin-top:24px;white-space:nowrap}
.attorney p{font-size:11px;font-style:italic;color:var(--muted);margin-top:6px}
.attorney .rule{height:3px;background:#cfcfcf;margin-top:10px}

/* testimonials */
.testi{left:0;top:2473px;width:1200px;height:561px;background:var(--light);clip-path:polygon(0 137px,50% 0,100% 137px,100% 100%,0 100%)}
.testi-title{top:2566px;color:var(--ink)}
.quote-badge{left:547px;top:2678px;width:93px;height:33px;background:var(--orange)}
.testi-head{left:0;top:2744px;width:1200px;text-align:center;font-family:"Playfair Display",serif;font-weight:700;font-size:20px;color:var(--orange)}
.testi-body{left:205px;top:2780px;width:790px;text-align:center;font-size:12px;line-height:19px;color:var(--muted)}
.arrow-btn{top:2772px;width:50px;height:50px;border-radius:50%;background:var(--white);border:1px solid #d6d6d6}
.avatar{left:555px;top:2851px;width:70px;height:70px;border-radius:50%;background:linear-gradient(160deg,#c8a488,#8a6a50)}
.testi-name{left:0;top:2938px;width:1200px;text-align:center;font-family:"Montserrat",sans-serif;font-weight:700;font-size:15px;color:var(--ink)}
.testi-role{left:0;top:2962px;width:1200px;text-align:center;font-family:"Montserrat",sans-serif;font-weight:600;font-size:9px;color:var(--orange);text-transform:uppercase}

/* map */
.map{left:0;top:3034px;width:1200px;height:423px;background:linear-gradient(135deg,#e6e6e6 0%,#d4d4d4 45%,#e9e9e9 70%,#d9d9d9 100%)}

/* contact */
.contact{left:0;top:3457px;width:1200px;height:588px;background:linear-gradient(120deg,#3b3b3b,#4b4b4b 50%,#333333)}
.contact-title{top:3510px;color:var(--white)}
.form-card{left:115px;top:3635px;width:432px;height:383px;background:var(--light);padding:22px 22px}
.form-card h3{font-family:"Montserrat",sans-serif;font-weight:400;font-size:22px;color:var(--ink)}
.form-card .field{position:absolute;left:22px;width:388px;height:38px;line-height:38px}
.form-card .msg{height:78px;line-height:30px}
.form-card .submit{position:absolute;left:322px;top:290px;width:99px;height:35px;background:var(--orange);color:var(--white);font-family:"Montserrat",sans-serif;font-size:12px;line-height:35px;text-align:center;text-transform:uppercase}
.company{left:599px;top:3635px;font-family:"Montserrat",sans-serif;font-weight:600;font-size:26px;color:var(--white);white-space:nowrap}
.office h4{font-family:"Montserrat",sans-serif;font-weight:600;font-size:17px;color:var(--white)}
.office-line{display:flex;gap:12px;margin-top:10px;font-size:12px;line-height:17px;color:#e4e4e4}
.pin{flex:none;width:24px;height:24px;border-radius:50%;background:var(--orange);display:flex;align-items:center;justify-content:center}
.book{left:896px;top:3897px;width:156px;height:58px;background:var(--orange);border-radius:4px;color:var(--white);font-family:"Montserrat",sans-serif;font-weight:600;font-size:14px;display:flex;align-items:center;justify-content:center;gap:10px;text-transform:uppercase}

/* footer */
.footer{left:0;top:4045px;width:1200px;height:55px;background:var(--orange);color:var(--white);font-size:13px;line-height:55px;text-align:center}
</style>
</head>
<body>

<!-- header -->
<div class="abs brand">PVT LAW GROUP PLLC</div>
<div class="abs brand-rule"></div>
<div class="abs contact-bar"></div>
<div class="abs contact-lines">240 N. 41ST ST. SUITE C. SEATTLE WA. 98110<br>206.555.0148 &nbsp;|&nbsp; FAX: 206.555.0149<br>PVTLEGALHOUSE.COM</div>

<nav class="abs nav">
  <a style="left:101px">Home</a>
  <a style="left:189px">Why PVT Law</a>
  <a style="left:350px">Family Law</a>
  <a style="left:481px">Civil Litigation</a>
  <a style="left:645px">Conveyancing</a>
  <a style="left:801px">Contact</a>
</nav>

<!-- hero -->
<div class="abs hero" role="img" aria-label="Photo of a person at a desk using a phone beside papers, a magazine and a coffee cup"></div>
<svg class="abs hero-edge" width="1200" height="525" viewBox="0 0 1200 525">
  <polygon points="0,525 1200,378 1200,395 0,525" fill="#d9d9d9"/>
</svg>
<div class="abs hero-card">
  <h1>At PVT Law, you are<br>our first priority</h1>
  <span class="btn-orange">Read more</span>
</div>

<!-- about -->
<h2 class="abs about-title"><b>ABOUT PVT</b> <span>LAW GROUP PLLC</span></h2>
<div class="abs about-rule"></div>
<div class="abs about-photo" role="img" aria-label="Photo of lawyers meeting around a table"></div>
<div class="abs about-sub">WHAT ARE OUR ADVANTAGES?</div>
<p class="abs about-lead">What does your company offer that will improve or solve a problem? Explain the pain point being alleviated right.</p>
<p class="abs about-body">What does your company offer that will improve or solve a problem? Explain the pain point being alleviated right.What does your company offer that will improve or solve a problem? Explain the pain point being alleviated right.</p>
<a class="abs read-more about-more">Read More &rarr;</a>

<div class="abs ask">
  <h2>Have a question?</h2>
  <div class="field" style="top:93px">Your Name</div>
  <div class="field" style="top:162px">Your Email</div>
  <div class="field" style="top:230px">Phone No.</div>
  <div class="btn-dark">Get started</div>
</div>

<!-- services -->
<section class="abs services">
  <h2 class="abs sec-title">Our Services</h2>
  <svg class="abs divider" style="top:140px" viewBox="0 0 660 30"><line x1="0" y1="15" x2="310" y2="15" stroke="#9a9a9a"/><line x1="350" y1="15" x2="660" y2="15" stroke="#9a9a9a"/><g fill="#ffffff"><rect x="324" y="4" width="8" height="8"/><rect x="334" y="14" width="8" height="8"/><rect x="318" y="14" width="8" height="8"/><rect x="326" y="20" width="8" height="8" opacity=".6"/></g></svg>

  <div class="abs svc" style="left:61px">
    <div class="svc-icon"><svg width="46" height="46" viewBox="0 0 46 46" fill="none" stroke="#fff" stroke-width="2.5"><rect x="8" y="6" width="24" height="34"/><line x1="13" y1="14" x2="27" y2="14"/><line x1="13" y1="21" x2="27" y2="21"/><line x1="13" y1="28" x2="22" y2="28"/><rect x="28" y="22" width="12" height="18"/></svg></div>
    <h3>Wills &amp; Estates</h3>
    <p>Estate planning is a process that involves examining your assets and liabilities, your personal and extended estate.</p>
    <a class="read-more">Read more &rarr;</a>
  </div>
  <div class="abs svc" style="left:345px">
    <div class="svc-icon"><svg width="46" height="46" viewBox="0 0 46 46" fill="none" stroke="#fff" stroke-width="2.5"><circle cx="23" cy="18" r="10"/><path d="M8 40c2-9 8-13 15-13s13 4 15 13"/><line x1="13" y1="18" x2="33" y2="18"/></svg></div>
    <h3>Civil Disputes</h3>
    <p>Estate planning is a process that involves examining your assets and liabilities, your personal and extended estate.</p>
    <a class="read-more">Read more &rarr;</a>
  </div>
  <div class="abs svc" style="left:629px">
    <div class="svc-icon"><svg width="46" height="46" viewBox="0 0 46 46" fill="none" stroke="#fff" stroke-width="2.5"><circle cx="23" cy="20" r="12"/><circle cx="23" cy="20" r="5"/><path d="M10 40h26"/><line x1="23" y1="32" x2="23" y2="40"/></svg></div>
    <h3>Family Law</h3>
    <p>Estate planning is a process that involves examining your assets and liabilities, your personal and extended estate.</p>
    <a class="read-more boxed">Read more &rarr;</a>
  </div>
  <div class="abs svc" style="left:900px">
    <div class="svc-icon"><svg width="46" height="46" viewBox="0 0 46 46" fill="none" stroke="#fff" stroke-width="2.5"><path d="M6 22 23 7l17 15"/><path d="M11 19v20h24V19"/><rect x="19" y="26" width="8" height="13"/></svg></div>
    <h3>Conveyancing</h3>
    <p>Estate planning is a process that involves examining your assets and liabilities, your personal and extended estate.</p>
    <a class="read-more">Read more &rarr;</a>
  </div>
</section>

<!-- attorneys -->
<section class="team">
  <h2 class="abs sec-title" style="top:1940px">Attorneys Team</h2>
  <svg class="abs divider" style="top:1990px" viewBox="0 0 660 30"><line x1="0" y1="15" x2="310" y2="15" stroke="#9a9a9a"/><line x1="350" y1="15" x2="660" y2="15" stroke="#9a9a9a"/><g fill="#222"><rect x="324" y="4" width="8" height="8"/><rect x="334" y="14" width="8" height="8"/><rect x="318" y="14" width="8" height="8"/><rect x="326" y="20" width="8" height="8" opacity=".6"/></g></svg>

  <div class="abs attorney" style="left:101px">
    <div class="attorney-photo" role="img" aria-label="Portrait of attorney Martin Hale in a dark suit" style="background:linear-gradient(160deg,#6b4a34,#b79270 50%,#2f2f36)"></div>
    <h3>Martin Hale</h3><p>Bar President / Criminal Lawyer</p><div class="rule"></div>
  </div>
  <div class="abs attorney" style="left:361px">
    <div class="attorney-photo" role="img" aria-label="Portrait of attorney Corinne Vale Ashby reading documents" style="background:linear-gradient(160deg,#5a3a2a,#c9a086 50%,#d7a9a0)"></div>
    <h3>Corinne Vale Ashby</h3><p>Associate / Family Lawyer</p><div class="rule"></div>
  </div>
  <div class="abs attorney" style="left:621px">
    <div class="attorney-photo" role="img" aria-label="Portrait of attorney Owen Marsh in a suit" style="background:linear-gradient(160deg,#e9e9e9,#c39b80 45%,#23262e)"></div>
    <h3>Owen Marsh</h3><p>Criminal Lawyer</p><div class="rule"></div>
  </div>
  <div class="abs attorney" style="left:881px">
    <div class="attorney-photo" role="img" aria-label="Portrait of attorney Helena Brookfield in a light blazer" style="background:linear-gradient(160deg,#f4f4f4,#d9b49a 45%,#e8e0d6)"></div>
    <h3>Helena Brookfield</h3><p>Employment Lawyer</p><div class="rule"></div>
  </div>
</section>

<!-- testimonials -->
<div class="abs testi"></div>
<h2 class="abs sec-title testi-title">Our Testimonials</h2>
<svg class="abs divider" style="top:2616px" viewBox="0 0 660 30"><line x1="0" y1="15" x2="310" y2="15" stroke="#9a9a9a"/><line x1="350" y1="15" x2="660" y2="15" stroke="#9a9a9a"/><g fill="#222"><rect x="324" y="4" width="8" height="8"/><rect x="334" y="14" width="8" height="8"/><rect x="318" y="14" width="8" height="8"/><rect x="326" y="20" width="8" height="8" opacity=".6"/></g></svg>
<svg class="abs quote-badge" viewBox="0 0 93 33"><rect width="93" height="33" fill="#f07022"/><text x="46.5" y="29" text-anchor="middle" font-family="Playfair Display, serif" font-size="30" font-weight="700" fill="#fff">&ldquo;</text></svg>
<div class="abs testi-head">At Trust, Each Lawyer Focuses Only On Civil Matters !</div>
<p class="abs testi-body">Our team explained every step of the dispute plainly and kept us informed from the first meeting to the final settlement. We felt heard, well prepared and fairly charged, and we would gladly return for any future legal matter.</p>
<svg class="abs arrow-btn" style="left:76px" viewBox="0 0 50 50"><circle cx="25" cy="25" r="24" fill="#fff" stroke="#d6d6d6"/><path d="M29 16l-9 9 9 9" fill="none" stroke="#777" stroke-width="2.5"/></svg>
<svg class="abs arrow-btn" style="left:1063px" viewBox="0 0 50 50"><circle cx="25" cy="25" r="24" fill="#fff" stroke="#d6d6d6"/><path d="M21 16l9 9-9 9" fill="none" stroke="#777" stroke-width="2.5"/></svg>
<div class="abs avatar" role="img" aria-label="Portrait of client Nadia Fairchild"></div>
<div class="abs testi-name">Nadia Fairchild</div>
<div class="abs testi-role">Corporate Lawyer</div>

<!-- map -->
<div class="abs map" role="img" aria-label="Street map showing the office location"></div>
<svg class="abs" style="left:482px;top:3160px" width="48" height="66" viewBox="0 0 48 66"><path d="M24 2C12 2 3 11 3 23c0 16 21 41 21 41s21-25 21-41C45 11 36 2 24 2z" fill="#f07022"/><circle cx="24" cy="23" r="11" fill="#fff"/><path d="M24 17v12M18 23h12" stroke="#f07022" stroke-width="3"/></svg>

<!-- contact -->
<section class="abs contact" role="img" aria-label="Dark toned office background photo"></section>
<h2 class="abs sec-title contact-title">Contact Us</h2>
<svg class="abs divider" style="top:3557px" viewBox="0 0 660 30"><line x1="0" y1="15" x2="310" y2="15" stroke="#8a8a8a"/><line x1="350" y1="15" x2="660" y2="15" stroke="#8a8a8a"/><g fill="#fff"><rect x="324" y="4" width="8" height="8"/><rect x="334" y="14" width="8" height="8"/><rect x="318" y="14" width="8" height="8"/><rect x="326" y="20" width="8" height="8" opacity=".6"/></g></svg>

<div class="abs form-card">
  <h3>Contact form</h3>
  <div class="field" style="top:79px">Name</div>
  <div class="field" style="top:134px">Email</div>
  <div class="field msg" style="top:190px">Message</div>
  <div class="submit">Submit</div>
</div>

<div class="abs company">A Full Service Technology Company.</div>

<div class="abs office" style="left:604px;top:3698px;width:250px">
  <h4>Head Office</h4>
  <div class="office-line"><span class="pin"><svg width="12" height="14" viewBox="0 0 12 14"><path d="M6 0C3 0 1 2 1 5c0 4 5 9 5 9s5-5 5-9c0-3-2-5-5-5z" fill="#fff"/></svg></span><span>1450 Larkspur Ave<br>Suite 310<br>North Ridgefield, NJ 07192</span></div>
  <div class="office-line"><span class="pin"><svg width="12" height="12" viewBox="0 0 12 12"><path d="M2 1l2 0 1 3-1.5 1a7 7 0 0 0 3.5 3.5L8 7l3 1v2c0 1-1 1-1 1C5 11 1 7 1 2c0 0 0-1 1-1z" fill="#fff"/></svg></span><span style="line-height:24px">Phone: +1 (732) 555-0187</span></div>
</div>
<div class="abs office" style="left:880px;top:3698px;width:260px">
  <h4>West Coast Office</h4>
  <div class="office-line"><span class="pin"><svg width="12" height="14" viewBox="0 0 12 14"><path d="M6 0C3 0 1 2 1 5c0 4 5 9 5 9s5-5 5-9c0-3-2-5-5-5z" fill="#fff"/></svg></span><span>4120 Harbor Point Drive<br>Suite 600<br>San Jose, CA 95134</span></div>
</div>
<div class="abs office" style="left:604px;top:3867px;width:260px">
  <h4>Technical Center</h4>
  <div class="office-line"><span class="pin"><svg width="12" height="14" viewBox="0 0 12 14"><path d="M6 0C3 0 1 2 1 5c0 4 5 9 5 9s5-5 5-9c0-3-2-5-5-5z" fill="#fff"/></svg></span><span>27610 W 12 Oak Road<br>Suite 180<br>Birchwood Hills MI 48390</span></div>
</div>
<div class="abs book"><svg width="26" height="20" viewBox="0 0 26 20" fill="none" stroke="#fff" stroke-width="2"><rect x="2" y="3" width="22" height="15" rx="2"/><line x1="2" y1="8" x2="24" y2="8"/><line x1="8" y1="1" x2="8" y2="5"/><line x1="18" y1="1" x2="18" y2="5"/></svg>Book now</div>

<footer class="abs footer">&copy; 2017 | PVT Law | All Right Reserved</footer>

</body>
</html>
```